Design a WordPress layout for a home loans company

The home loans company in question is going through a rebrand and needs a new website layout.
Sites they like: http://www.brightkeylending.example.au/
Current logo: Attached.
Colours to be used: As per those used in logo.
Primary: #71aa3d
Secondary: #130e10
Pages to be designed:
- Homepage
- Internal services page
Menu items for display purposes:
- Home
- About Us
- Speak to a Broker
- Articles
- Contact Us
A modern design with simplicity is key.
For copy, dummy text such as Lorem ipsum will be fine.
If you would like anything elso, please ask.
Target Market(s)
25-40 year old
Mostly female
Buying their first home in most cases
Industry/Entity Type
Mortgage Brokerage
Number of Pages Required
2 page

```html
<!DOCTYPE html>
<html lang="en">
<head>
<meta charset="utf-8">
<title>Brightkey Home Loans</title>
<link href="https://fonts.googleapis.com/css2?family=Lato:wght@400;700;900&family=Montserrat:wght@600;700&display=swap" rel="stylesheet">
<style>
:root{
  --green:#71aa3d;
  --green-dark:#4f8a2a;
  --green-deep:#3f7424;
  --black:#130e10;
  --ink:#222;
  --grey:#8a8a8a;
  --white:#fff;
  --footer:#1d1f22;
}
*{box-sizing:border-box;margin:0;padding:0}
html,body{width:1200px;height:3982px;overflow:hidden}
body{font-family:'Lato',sans-serif;color:var(--ink);background:var(--white)}
section,header,footer{position:relative;width:1200px;overflow:hidden}
.btn{display:inline-block;font-family:'Lato',sans-serif;font-weight:700;font-size:20px;text-transform:uppercase;padding:16px 28px;border:0}
.btn-white{background:var(--white);color:var(--black)}
.btn-green{background:var(--green);color:var(--white);border:2px solid var(--green-dark)}
.brand-name{font-family:'Lato',sans-serif;font-weight:900;color:var(--green);display:flex;align-items:center;gap:12px}
.brand-name .dot{width:14px;height:14px;background:var(--green)}

/* header */
.site-header{height:125px;background:var(--black);display:flex;align-items:center;padding:0 78px}
.site-header .brand-name{font-size:36px}
.main-nav{margin-left:auto;display:flex;gap:46px;font-size:17px;text-transform:uppercase;color:#9a9a9a}
.main-nav .active{color:var(--white)}
.search-icon{margin-left:40px;padding-left:24px;border-left:1px solid #444}

/* hero */
.hero{height:573px;background:linear-gradient(100deg,#5a4a3c 0%,#8b7561 35%,#6d6a66 60%,#3e3a38 100%)}
.hero-photo{position:absolute;inset:0}
.hero-copy{position:absolute;right:80px;top:150px;width:500px;text-align:right;color:var(--white)}
.hero-copy h1{font-family:'Montserrat',sans-serif;font-weight:700;font-size:46px;line-height:1.12;text-transform:uppercase}
.hero-copy h1 .big{font-size:56px}
.hero-copy p{font-size:16px;line-height:1.55;margin:16px 0 26px;text-align:left}

/* find broker */
.find-broker{height:192px;background:var(--green);text-align:center;color:var(--white)}
.find-broker h2{font-size:40px;font-weight:900;padding-top:36px}
.broker-form{display:flex;justify-content:center;gap:6px;margin-top:26px}
.broker-form .field{width:375px;height:50px;background:rgba(255,255,255,.35);color:#e8f3dc;font-size:15px;text-align:left;padding:15px 20px}
.broker-form .btn{padding:14px 34px;font-size:18px}

/* about */
.about{height:496px;background:var(--white)}
.about-copy{position:absolute;left:78px;top:110px;width:610px}
.section-title{font-size:42px;font-weight:900;color:var(--green)}
.body-text{font-size:15px;line-height:1.6;color:var(--grey)}
.about-copy .body-text{margin:22px 0 34px}
.about-house{position:absolute;right:0;top:30px;width:520px;height:466px;background:linear-gradient(160deg,#1f2428 0%,#3b4148 55%,#6a7c3c 88%,#4c7a25 100%)}

/* advice */
.advice{height:512px;background:var(--green);color:var(--white)}
.advice-photo{position:absolute;left:78px;top:70px;width:496px;height:372px;border-radius:180px 60px 180px 60px;border-bottom:5px solid #e0b426;background:linear-gradient(120deg,#e7e2d8 0%,#c9c4bb 40%,#8f6d4d 70%,#5e7aa0 100%)}
.advice-copy{position:absolute;left:602px;top:100px;width:520px}
.advice-copy h2{font-size:40px;font-weight:900;line-height:1.1}
.advice-copy .body-text{color:#eef6e6;margin:22px 0 30px}

/* benefits */
.benefits{height:452px;background:linear-gradient(180deg,#2a2226,#1a1416);text-align:center;color:var(--white)}
.benefits h2{font-size:40px;font-weight:900;padding-top:62px}
.benefits .lead{font-size:15px;color:#888;margin-top:22px}
.benefit-cards{display:flex;justify-content:center;gap:18px;margin-top:34px}
.benefit-card{width:340px;height:210px;background:var(--white);text-align:left;padding:30px 24px}
.benefit-card .head{display:flex;align-items:center;gap:14px;color:var(--black);font-size:19px;font-weight:900}
.benefit-card .body-text{margin-top:28px;font-size:14px}

/* compare */
.compare{height:425px;background:linear-gradient(180deg,var(--green-dark),var(--green-deep));text-align:center;color:var(--white)}
.compare h2{font-size:40px;font-weight:900;padding-top:90px}
.compare p{font-size:15px;line-height:1.6;width:700px;margin:22px auto 0}
.compare .btn{margin-top:26px;font-size:19px;padding:14px 22px}

/* articles */
.articles{height:470px;text-align:center}
.articles .section-title{padding-top:50px}
.article-list{display:flex;justify-content:center;gap:22px;margin-top:30px}
.article{width:346px;text-align:left}
.article-photo{height:146px;border:2px solid #444}
.article h3{font-size:16px;font-weight:900;margin-top:12px;color:var(--black)}
.article.featured h3{color:var(--green)}
.article p{font-size:14px;color:#666;margin-top:12px;line-height:1.5}
.article .more{font-size:13px;font-weight:700;margin-top:12px;text-transform:uppercase;color:var(--black)}
.article.featured .more{color:var(--green);text-decoration:underline}

/* newsletter */
.newsletter{height:318px;background:linear-gradient(180deg,#7bb548,var(--green-dark));text-align:center;color:var(--white)}
.newsletter h2{font-size:40px;font-weight:900;padding-top:70px}
.newsletter p{font-size:15px;color:#e3f0d6;margin-top:14px}
.subscribe{width:686px;height:42px;margin:28px auto 0;border:1px solid rgba(255,255,255,.7);display:flex;align-items:center;justify-content:space-between;padding:0 12px 0 18px;font-size:14px}

/* footer */
.site-footer{height:327px;background:linear-gradient(180deg,var(--footer),#0f1012);color:var(--white)}
.footer-title{font-size:20px;font-weight:900}
.quick-links{position:absolute;left:78px;top:50px}
.quick-links .cols{display:flex;gap:60px;margin-top:30px}
.quick-links ul{list-style:none;font-size:14px;color:#aaa;line-height:2.2}
.quick-links li::before{content:"›";margin-right:10px;color:#ccc}
.footer-brand{position:absolute;left:440px;top:130px;font-size:54px}
.footer-brand .dot{width:18px;height:18px}
.contact{position:absolute;left:846px;top:50px;width:300px}
.contact-row{display:flex;gap:24px;margin-top:26px;font-size:14px;color:#aaa;line-height:1.5}
.contact-row svg{flex:none}
.copyright{height:92px;background:#0a0a0a;color:#aaa;text-align:center;font-size:14px;line-height:92px}
.copyright b{color:var(--green)}
</style>
</head>
<body>

<header class="site-header">
  <div class="brand-name"><span class="dot"></span>Brightkey Home Loans</div>
  <nav class="main-nav">
    <span class="active">Home</span><span>About</span><span>Speak to a Broker</span><span>Articles</span><span>Contact</span>
  </nav>
  <div class="search-icon">
    <svg width="26" height="26" viewBox="0 0 26 26"><circle cx="11" cy="11" r="8" fill="none" stroke="#fff" stroke-width="3"/><line x1="17" y1="17" x2="24" y2="24" stroke="#fff" stroke-width="3"/></svg>
  </div>
</header>

<section class="hero">
  <div class="hero-photo" role="img" aria-label="Smiling couple looking at a tablet at home"></div>
  <div class="hero-copy">
    <h1>Are you looking<br>for <span class="big">Home Loan?</span></h1>
    <p>Lorem Ipsum is simply dummy text of the printing and typesetting industry. Lorem Ipsum has been the industry's standard dummy.</p>
    <span class="btn btn-white">Find out more</span>
  </div>
</section>

<section class="find-broker">
  <h2>Find a Local Broker :</h2>
  <div class="broker-form">
    <div class="field">Email</div>
    <div class="field">Enter Location Or Postcode</div>
    <span class="btn btn-white">Find Broker</span>
  </div>
</section>

<section class="about">
  <div class="about-copy">
    <h2 class="section-title">About Brightkey Home Loans</h2>
    <p class="body-text">Lorem Ipsum is simply dummy text of the printing and typesetting industry. Lorem Ipsum has been the industry's standard dummy text ever since the 1500s, when an unknown printer took a galley of type and scrambled it to make a type specimen book. It has survived not only five centuries, but also the leap into electronic typesetting, remaining essentially unchanged. It was popularised in the 1960s.It has survived not only five centuries.</p>
    <span class="btn btn-green">Learn more</span>
  </div>
  <div class="about-house" role="img" aria-label="Modern two-storey house lit at dusk on a green lawn"></div>
</section>

<section class="advice">
  <div class="advice-photo" role="img" aria-label="Broker and client reviewing plans at a desk"></div>
  <div class="advice-copy">
    <h2>Better advice through<br>better listening</h2>
    <p class="body-text">Lorem Ipsum is simply dummy text of the printing and typesetting industry. Lorem Ipsum has been the industry's standard dummy text ever since the 1500s, when an unknown printer took a galley of type and scrambled it to make a type specimen book. It has survived not only five centuries, but also the leap into electronic typesetting, remaining essentially unchanged. It was popularised in the 1960s.It has survived not only five centuries.</p>
    <span class="btn btn-white">Learn more</span>
  </div>
</section>

<section class="benefits">
  <h2>With a Brightkey Home Loans broker, you'll have</h2>
  <p class="lead">Lorem Ipsum is simply dummy text of the printing and typesetting industry.</p>
  <div class="benefit-cards">
    <div class="benefit-card">
      <div class="head"><svg width="40" height="44" viewBox="0 0 40 44"><path d="M20 4a12 12 0 0 0-12 12c0 9 12 22 12 22s12-13 12-22A12 12 0 0 0 20 4z" fill="none" stroke="#71aa3d" stroke-width="3"/><circle cx="20" cy="16" r="4" fill="#71aa3d"/><ellipse cx="20" cy="40" rx="14" ry="3" fill="none" stroke="#71aa3d" stroke-width="2"/></svg>Local experts</div>
      <p class="body-text">Lorem Ipsum is simply dummy text of the printing and typesetting industry. Lorem Ipsum has been the industry's standard dummy text.</p>
    </div>
    <div class="benefit-card">
      <div class="head"><svg width="40" height="44" viewBox="0 0 40 44"><circle cx="20" cy="22" r="16" fill="#71aa3d"/><path d="M14 22l5 5 9-10" fill="none" stroke="#fff" stroke-width="3.5"/></svg>Ongoing trusted advice</div>
      <p class="body-text">Lorem Ipsum is simply dummy text of the printing and typesetting industry. Lorem Ipsum has been the industry's standard dummy text.</p>
    </div>
    <div class="benefit-card">
      <div class="head"><svg width="40" height="44" viewBox="0 0 40 44"><rect x="4" y="20" width="8" height="18" fill="#71aa3d"/><path d="M14 20l8-14c3 0 4 2 3 6l-1 6h10c2 0 3 2 2 4l-4 14H14z" fill="#71aa3d"/></svg>Greater choice</div>
      <p class="body-text">Lorem Ipsum is simply dummy text of the printing and typesetting industry. Lorem Ipsum has been the industry's standard dummy text.</p>
    </div>
  </div>
</section>

<section class="compare">
  <h2>Compare hundreds of home loan options</h2>
  <p>At Brightkey we understand the home loan market can be confusing.<br><br>That's why our unique comparison tool makes it easy to compare home loans from a range of lenders.</p>
  <span class="btn btn-white">Compare your home loan options</span>
</section>

<section class="articles">
  <h2 class="section-title">Articles</h2>
  <div class="article-list">
    <article class="article featured">
      <div class="article-photo" role="img" aria-label="Family in a bright new living room" style="background:linear-gradient(135deg,#f2f2f0,#cfd6dc)"></div>
      <h3>Lorem Ipsum is simply dummy text of the printing.</h3>
      <p>Lorem Ipsum is simply dummy text of the printing and typesetting.</p>
      <div class="more">Read more</div>
    </article>
    <article class="article">
      <div class="article-photo" role="img" aria-label="Family relaxing on a sofa with a dog" style="background:linear-gradient(135deg,#dfe6ee,#9c7a5d)"></div>
      <h3>Lorem Ipsum is simply dummy text of the printing.</h3>
      <p>Lorem Ipsum is simply dummy text of the printing and typesetting.</p>
      <div class="more">Read more</div>
    </article>
    <article class="article">
      <div class="article-photo" role="img" aria-label="Hand holding a small model house" style="background:linear-gradient(135deg,#ffffff,#d9c7bb)"></div>
      <h3>Lorem Ipsum is simply dummy text of the printing.</h3>
      <p>Lorem Ipsum is simply dummy text of the printing and typesetting.</p>
      <div class="more">Read more</div>
    </article>
  </div>
</section>

<section class="newsletter">
  <h2>Subscribe Newsletter</h2>
  <p>Sign up to be the first to hear about us</p>
  <div class="subscribe"><span>Email Id</span>
    <svg width="20" height="20" viewBox="0 0 20 20"><path d="M2 10L18 3l-5 15-3-6z" fill="none" stroke="#fff" stroke-width="1.5"/></svg>
  </div>
</section>

<footer class="site-footer">
  <div class="quick-links">
    <div class="footer-title">Quick Links</div>
    <div class="cols">
      <ul><li>Home</li><li>About</li><li>Client Login</li><li>Compliments</li><li>Privacy Policy</li></ul>
      <ul><li>Sitemap</li><li>Contact Us</li><li>My Account</li></ul>
    </div>
  </div>
  <div class="brand-name footer-brand"><span class="dot"></span>Brightkey</div>
  <div class="contact">
    <div class="footer-title">Contact Us</div>
    <div class="contact-row"><svg width="18" height="22" viewBox="0 0 18 22"><path d="M9 1a7 7 0 0 0-7 7c0 6 7 13 7 13s7-7 7-13a7 7 0 0 0-7-7z" fill="#71aa3d"/><circle cx="9" cy="8" r="2.5" fill="#1d1f22"/></svg><span>123 lorem ipsum dummy text,<br>Street,near place,<br>Country - 123456.</span></div>
    <div class="contact-row"><svg width="18" height="22" viewBox="0 0 18 22"><rect x="3" y="1" width="12" height="20" rx="2" fill="none" stroke="#71aa3d" stroke-width="2"/><circle cx="9" cy="17" r="1.3" fill="#71aa3d"/></svg><span>123 456 7878</span></div>
    <div class="contact-row"><svg width="18" height="22" viewBox="0 0 18 22"><circle cx="9" cy="11" r="8" fill="none" stroke="#71aa3d" stroke-width="2"/><path d="M9 6v5l3 2" fill="none" stroke="#71aa3d" stroke-width="2"/></svg><span>Monday-Friday : 7 am - 4 pm<br>Saturday-Sunday : Closed</span></div>
  </div>
</footer>

<div class="copyright">© <b>Brightkey Home Loans</b> - 2018. All Rights Reserved.</div>

</body>
</html>
```